依頼詳細
既に当塾のロゴはございますので、使用してください。
使用ソフトはアドビPhotoshopを使用してください。

発注する会社は「紙問屋柚」様です。
https://www.kamiyuzu-shop.jp/item_detail/detail.html?bcd1=000000&bcd2=005182&scd=207411865
この会社にはテンプレートファイルがございますので、こちらをご使用ください。
(テンプレートファイルは上記URLから得てください。)
記載項目
表面:塾のロゴ・当塾の住所
〒109-0087
東京都港区白楓台7-2-19
白楓台ソレイユ館514号
株式会社楢崎塾

裏面:なし
希望イメージ
シンプル 複雑
単色 カラフル
暗い 明るい
日常 高級
遊び心 厳粛
未来的 伝統的
女性的 男性的
希望する色
青系
納品ファイル
• フォトショップ形式 (.psd)
補足説明
デザインの著作権は当塾に帰属するものとします。
著作権はお譲りいただき、著作者人格権は行使しないことをご了承ください。
【追記20200815】
たくさんのご応募ありがとうございます。
・電話番号を書いていただけるランサー様がいらっしゃいました。
当塾の電話番号は06-6907-4815です。記載いただいても結構です。

また追記いたします。
質問等ございましたら、なんでもおっしゃって下さい。
【20200819】
写真を追加して欲しいという依頼がありましたので、写真を追加いたします。
私としては、写真は少し恥ずかしいような気もします。
似顔絵などでしたら面白いと思います。

どうぞよろしくお願いいたします。
【追記20200820】
さまざまなご提案、ありがとうございます。
・切手に関しまして、当塾では料金後納などではなく、一枚一枚切手を貼っております。
・フリー素材のイラストを入れてくださる方がいらっしゃいました。親しみやすくて良いと思いますが、しばらく使いますので、飽きの来ないデザインですと助かります。
【追記20200825】
たくさんのご提案ありがとうございます。
木曜日~土曜日に選定作業をさせていただく予定です。
どうぞよろしくお願いいたします。
【追記20200828】
封筒デザインに関しまして、たくさんのデザインありがとうございます。
現在選定中です。8月中には決定できると思いますので、少しお待ちください。

弊社スタッフの多数決と、横のタイプの方がより多くの情報を詰め込めるということで、当選させていただきました。
次点には、デザインの秀逸な方と修正依頼に真摯に応じていただけた方を選ばせていただきました。

さまざまなご提案、ありがとうございました。
引き続きよろしくお願いいたします。

```html
<!DOCTYPE html>
<html lang="ja">
<head>
<meta charset="utf-8">
<title>楢崎塾 長形封筒デザイン</title>
<link href="https://fonts.googleapis.com/css2?family=Noto+Sans+JP:wght@400;500;700;900&display=swap" rel="stylesheet">
<style>
  :root {
    --backdrop: #e4e4e4;
    --paper: #ffffff;
    --paper-edge: #d2d2d2;
    --brand-blue: #1f4f9e;
    --accent-orange: #e8772e;
    --ink: #555555;
    --guide: #9a9a9a;
  }
  html, body {
    margin: 0;
    padding: 0;
    width: 838px;
    height: 1200px;
    overflow: hidden;
    background: var(--backdrop);
    font-family: "Noto Sans JP", sans-serif;
  }
  .canvas {
    position: relative;
    width: 838px;
    height: 1200px;
  }
  .envelope-shape {
    position: absolute;
    left: 0;
    top: 0;
  }
  .stamp {
    position: absolute;
    left: 196px;
    top: 226px;
    width: 68px;
    height: 74px;
    background: linear-gradient(160deg, #f6d36a 0%, #e9553f 55%, #5aa05c 100%);
    outline: 4px solid #f3efe3;
  }
  .address-window {
    position: absolute;
    left: 246px;
    top: 428px;
    width: 404px;
    height: 146px;
    border-top: 1.5px solid var(--guide);
    border-bottom: 1.5px solid var(--guide);
    color: var(--guide);
    font-size: 11px;
    letter-spacing: 1px;
  }
  .address-window .zip { position: absolute; left: 12px; top: 10px; }
  .address-window .line { position: absolute; left: 12px; }
  .address-window .line-1 { top: 32px; }
  .address-window .line-2 { top: 50px; }
  .address-window .recipient {
    position: absolute;
    left: 12px;
    top: 100px;
    font-size: 18px;
    letter-spacing: 4px;
  }
  .sender {
    position: absolute;
    left: 184px;
    top: 790px;
    width: 300px;
  }
  .sender-brand {
    display: flex;
    align-items: center;
    gap: 8px;
    color: var(--brand-blue);
    font-weight: 900;
    font-size: 34px;
    line-height: 1;
  }
  .sender-brand .mark {
    width: 34px;
    height: 34px;
    background: var(--brand-blue);
  }
  .sender-tagline {
    margin-top: 58px;
    font-size: 11.5px;
    color: var(--accent-orange);
    font-weight: 500;
  }
  .sender-address {
    margin-top: 4px;
    font-size: 9.5px;
    line-height: 1.5;
    color: var(--ink);
  }
  .sender-company {
    margin-top: 2px;
    font-size: 14px;
    color: var(--ink);
    font-weight: 500;
  }
  .sender-tel {
    font-size: 10px;
    color: var(--ink);
  }
  .sender-web {
    margin-top: 4px;
    font-size: 17px;
    color: var(--accent-orange);
    letter-spacing: 0.5px;
  }
  .student-photo {
    position: absolute;
    left: 444px;
    top: 712px;
    width: 226px;
    height: 262px;
    background: radial-gradient(ellipse at 55% 55%, #d9dde6 0%, #eef0f4 55%, rgba(255,255,255,0) 75%);
  }
</style>
</head>
<body>
<div class="canvas">
  <svg class="envelope-shape" width="838" height="1200" viewBox="0 0 838 1200" aria-hidden="true">
    <path d="M196 44 L642 44 L678 210 L162 210 Z" fill="var(--paper)" stroke="var(--paper-edge)" stroke-width="1"/>
    <rect x="162" y="210" width="516" height="906" fill="var(--paper)" stroke="var(--paper-edge)" stroke-width="1"/>
    <line x1="162" y1="210" x2="678" y2="210" stroke="var(--paper-edge)" stroke-width="1"/>
  </svg>

  <div class="stamp" role="img" aria-label="花束の絵柄の切手"></div>

  <div class="address-window">
    <span class="zip">〒000-0000</span>
    <span class="line line-1">○○○○○○○○○○○○○○○○○○○○○○○○○○○○</span>
    <span class="line line-2">○○○○○○○○○○○○○○○○○○○○○○○○○</span>
    <span class="recipient">○○ ○○ 様</span>
  </div>

  <div class="student-photo" role="img" aria-label="制服姿で元気にジャンプする生徒の写真と「よーし、勉強頑張るぞー！」の吹き出し文字"></div>

  <div class="sender">
    <div class="sender-brand"><span class="mark"></span><span>楢崎塾</span></div>
    <div class="sender-tagline">オンライン家庭教師サービス / 個別指導専門塾</div>
    <div class="sender-address">〒109-0087 東京都港区白楓台7-2-19 白楓台ソレイユ館514号</div>
    <div class="sender-company">株式会社楢崎塾</div>
    <div class="sender-tel">TEL 06-6907-4815</div>
    <div class="sender-web">www.narasakijyuku.com</div>
  </div>
</div>
</body>
</html>
```